Cobalt Business Card Designs***

WE ARE A FULL SERVICE FACILITY. ALL KINDS OF CAR/ TRK, REPAIR. CUSTOM WHEELS & TIRES. BRAKES, MUFFLERS, SHOCK, STRUTS...BATTERIES, STARTERS, ATERNATORS, TUNE UPS (WE DO IT ALL) ESTABLISHED IN 2004, LOCALLY OWNED AND OPERATED.... I AM OPEN TO SUGGESTIONS AS WELL ON ANY IDEAS

Contact Information for Business Card

WE DO COMPLETE AUTO REPAIR AND WHEELS, TIRES AND ACCESSORIES AT OUR STORE. I NAME OF SHOP (COBALT MOTORWORKS GROUP) WOULD LIKE OUR EMAIL ON IT (COBALTMOTORGROUP@QUIVEL.NET) PHONE NUMBER 419-555-WREN (9736) BUSINESS HOURS MON- FRI 7:30-5 INSTAGRAM LOGO WITH (@COBALT_MOTOR_GARAGE) WEBSITE (HARBORWHEELSANDTREADS.COM)FACEBOOK LOGO W/ (FACEBOOK.COM/COBALTMOTORWORKS) AN A+/ QRF LOGO (THE LITTLE TORCH)... MAYBE EVEN EST.2004 INSIDE OF A "POW SIGN" (UNLESS IT GETS TO CLUTTERED) AND ON THE BACK OF THE CARD MAYBE A FAINT PICTURE OF "SOMETHING" IN BACKGROUND BUT STILL BE ABLE TO SEE THE ESTIMATE WE WRITE ON THE BACK. I WOULD LIKE ON THE BACK, DOWN IN THE RIGHT HAND CORNER A SPOT FOR A DATE AND INT. WE ALSO EXCEPT: KORA, PLENTIPAY, TRAVELLO AND ZIPWELL

```html
<!DOCTYPE html>
<html lang="en">
<head>
<meta charset="utf-8">
<title>Cobalt Motorworks Group – Business Card</title>
<link href="https://fonts.googleapis.com/css2?family=Roboto+Condensed:wght@400;700&display=swap" rel="stylesheet">
<style>
  :root{
    --stage:#000;
    --card:#e6e6e8;
    --ink:#111;
    --brand-blue:#1f5fc4;
    --hours-blue:#2b3a8f;
    --burst:#1aa7e6;
    --muted:#bdbdc2;
    --rule:#333;
  }
  html,body{margin:0;padding:0;overflow:hidden;background:var(--stage);}
  .canvas{position:relative;width:1200px;height:1200px;background:var(--stage);overflow:hidden;
    font-family:"Roboto Condensed",Arial,sans-serif;color:var(--ink);}
  .card{position:absolute;left:240px;width:720px;height:430px;overflow:hidden;background:var(--card);}
  .card--front{top:160px;}
  .card--back{top:690px;}
  .photo{position:absolute;inset:0;}
  .photo--engine{background:radial-gradient(ellipse at 45% 25%,#f4f4f6 0%,#d9d9dd 35%,#c9c7cc 60%,#d8d6da 100%);}
  .photo--wheels{background:linear-gradient(180deg,#f3f3f5 0%,#dedee2 50%,#ececef 100%);}
  .band{position:absolute;left:0;right:0;top:180px;height:132px;background:rgba(255,255,255,.55);}
  .abs{position:absolute;white-space:nowrap;}
  .wordmark{font-weight:700;color:var(--brand-blue);letter-spacing:2px;line-height:1;}
  .tagline{font-weight:400;color:var(--ink);letter-spacing:4px;line-height:1;}
  .hours{color:var(--hours-blue);font-size:24px;}
  .divider{position:absolute;height:3px;background:linear-gradient(90deg,transparent,#333 20%,#aaa 50%,#333 80%,transparent);}

  .contact-row{position:absolute;left:0;right:0;display:flex;justify-content:center;align-items:center;}
  .contact{font-size:17px;display:flex;align-items:center;gap:6px;white-space:nowrap;padding:0 9px;line-height:1;}
  .contact + .contact{border-left:1px solid var(--rule);}
  .contact-row--main .contact{height:52px;}
  .contact-row--social .contact{height:52px;}
  .square{width:24px;height:24px;background:#555;border-radius:4px;display:inline-block;flex:none;}
  .badge{width:22px;height:34px;background:#4a8fb8;border-radius:3px;display:inline-block;}

  .burst{position:absolute;left:480px;top:174px;width:180px;height:90px;}
  .burst text{font-family:"Roboto Condensed",Arial,sans-serif;font-size:27px;fill:#fff;}
  .pay{position:absolute;top:332px;height:41px;display:flex;align-items:center;justify-content:center;
    background:#fff;border:1px solid #999;font-size:12px;font-weight:700;color:#333;}
  .pay--round{border-radius:50%;width:43px;font-size:9px;}
  .stamp{font-size:18px;}
  .stamp .hint{color:var(--muted);}
</style>
</head>
<body>
<div class="canvas">

  <section class="card card--front">
    <div class="photo photo--engine" role="img" aria-label="Faded photo of a chrome engine bay"></div>
    <div class="abs wordmark" style="left:0;right:0;text-align:center;top:90px;font-size:72px;">COBALT</div>
    <div class="abs tagline" style="left:0;right:0;text-align:center;top:150px;font-size:38px;">MOTORWORKS GROUP</div>
    <div class="abs hours" style="left:0;right:0;text-align:center;top:188px;">BUSINESS HOURS MON- FRI 7:30-5</div>
    <div class="divider" style="left:6px;right:8px;top:234px;"></div>

    <div class="contact-row contact-row--main" style="top:248px;">
      <div class="contact">
        <svg width="24" height="24" viewBox="0 0 24 24" aria-hidden="true"><path fill="#111" d="M6.6 10.8a15 15 0 0 0 6.6 6.6l2.2-2.2c.3-.3.7-.4 1-.2 1.1.4 2.3.6 3.6.6.6 0 1 .4 1 1V20c0 .6-.4 1-1 1A17 17 0 0 1 3 4c0-.6.4-1 1-1h3.5c.6 0 1 .4 1 1 0 1.3.2 2.5.6 3.6.1.3 0 .7-.2 1z"/></svg>
        419-555-WREN (9736)
      </div>
      <div class="contact">
        <svg width="36" height="30" viewBox="0 0 36 30" aria-hidden="true"><circle cx="18" cy="15" r="15" fill="#111"/><text x="18" y="19" font-size="12" font-weight="700" fill="#fff" text-anchor="middle" font-family="Roboto Condensed, sans-serif">www</text></svg>
        harborwheelsandtreads.com
      </div>
      <div class="contact">
        <svg width="32" height="22" viewBox="0 0 34 24" aria-hidden="true"><rect x="1" y="1" width="32" height="22" fill="none" stroke="#111" stroke-width="2"/><path d="M1 1l16 13L33 1M1 23l12-11M33 23L21 12" fill="none" stroke="#111" stroke-width="2"/></svg>
        cobaltmotorgroup@quivel.net
      </div>
    </div>

    <div class="contact-row contact-row--social" style="top:299px;">
      <div class="contact"><span class="square"></span>@cobalt_motor_garage</div>
      <div class="contact"><span class="square"></span>@cobaltmotorworks</div>
      <div class="contact"><span class="badge" role="img" aria-label="Accreditation badge"></span></div>
    </div>

    <div class="contact-row" style="top:356px;">
      <div class="contact">
        <svg width="20" height="28" viewBox="0 0 22 30" aria-hidden="true"><path fill="#111" d="M11 0a11 11 0 0 0-11 11c0 8 11 19 11 19s11-11 11-19A11 11 0 0 0 11 0zm0 15a4 4 0 1 1 0-8 4 4 0 0 1 0 8z"/></svg>
        4718 W. Harrow Ave. Millbrook, OH 43999
      </div>
    </div>
  </section>

  <section class="card card--back">
    <div class="photo photo--wheels" role="img" aria-label="Faded row of custom alloy wheels"></div>
    <div class="band"></div>
    <div class="abs wordmark" style="left:135px;top:182px;font-size:58px;">COBALT</div>
    <div class="abs tagline" style="left:135px;top:232px;font-size:29px;letter-spacing:3px;">MOTORWORKS GROUP</div>
    <div class="abs" style="left:168px;top:265px;font-size:18px;">4718 W. Harrow Ave. Millbrook, OH 43999</div>
    <svg class="burst" viewBox="0 0 180 90" aria-hidden="true">
      <polygon fill="var(--burst)" points="90,0 104,18 128,8 132,28 172,34 148,48 174,62 132,62 122,86 98,70 70,84 66,62 14,64 40,50 6,36 52,30 58,8 80,20"/>
      <text x="90" y="54" text-anchor="middle">EST.2004</text>
    </svg>
    <div class="divider" style="left:0;right:0;top:310px;"></div>

    <div class="pay pay--round" style="left:82px;">ZIPWELL</div>
    <div class="pay" style="left:133px;width:63px;">PLENTIPAY</div>
    <div class="pay" style="left:205px;width:63px;">KORA</div>
    <div class="pay" style="left:275px;width:63px;">TRAVELLO</div>

    <div class="abs stamp" style="left:508px;top:331px;">DATE : <span class="hint">DD/MM/YYYY</span></div>
    <div class="abs stamp" style="left:508px;top:351px;">INT :</div>
  </section>

</div>
</body>
</html>
```